Banner ad series

We need a series of banner ads for 4 different digital products. The ads will drive traffic to these landing pages:
Relocate.set: http://tidyhearthgoods.example/relocateset/
Treasures.log: http://tidyhearthgoods.example/digital-treasures-log/
Jumpwise Boot Camp: http://tidyhearthgoods.example/jumpwise-boot-camp/
Vital Rhythm Boot Camp: http://tidyhearthgoods.example/vital-rhythm/

Banner Ad Sizes needed:
160x600, 728x90, 300x250

Text files with the copy/variations needed for each product are attached. In the text file - the first line of each option is the main headline. All other copy is support copy and OPTIONAL.

Target Market(s)

Our target market is a woman between the ages of 30-55 with kids. She's smart, working professionally and always on the lookout for products and services that will help her get more organized.

Industry/Entity Type

Digital

Requirements
Must have
• Tidy Hearth logo

```html
<!DOCTYPE html>
<html lang="en">
<head>
<meta charset="utf-8">
<title>Tidy Hearth Boot Camp Banner Series</title>
<link rel="stylesheet" href="https://fonts.googleapis.com/css2?family=Roboto+Condensed:wght@300;400;700&display=swap">
<style>
  :root {
    --board: #000000;
    --label: #c9c9c9;
    --white: #ffffff;
    --green: #8cc63f;
    --green-dark: #2f7a3a;
    --pink: #d9214f;
    --pink-soft: #e23a6a;
    --ink: #2b2b2b;
    --photo-light: #f1f0ec;
    --photo-mid: #d6d4cc;
  }
  * { margin: 0; padding: 0; box-sizing: border-box; }
  html, body {
    width: 1200px; height: 1171px; overflow: hidden;
    background: var(--board);
    font-family: "Roboto Condensed", "Arial Narrow", sans-serif;
  }
  .board {
    position: absolute; left: 0; top: 0;
    width: 820px; height: 800px;
    transform: scale(1.46341);
    transform-origin: 0 0;
  }
  .size-label {
    position: absolute;
    color: var(--label);
    font-weight: 400;
    font-size: 22px;
    letter-spacing: 0.5px;
  }
  .banner { position: absolute; overflow: hidden; background: var(--white); }

  .brand {
    position: absolute;
    display: flex; align-items: center; justify-content: center;
  }
  .brand-name { color: var(--ink); font-weight: 400; font-size: 20px; white-space: nowrap; }

  .headline {
    position: absolute; color: var(--ink);
    font-weight: 300; text-transform: uppercase; line-height: 1;
  }
  .support { position: absolute; font-weight: 700; line-height: 1.3; }

  .photo {
    position: absolute;
    border: 3px solid var(--white);
    border-radius: 6px;
    background: linear-gradient(160deg, var(--photo-light) 0%, var(--photo-mid) 60%, #b9c98f 100%);
    box-shadow: 0 1px 4px rgba(0,0,0,0.35);
  }
  .cta {
    position: absolute;
    background: var(--pink);
    border: 2px solid var(--white);
    border-radius: 6px;
    color: var(--white);
    font-weight: 700; font-size: 11px;
    display: flex; align-items: center; justify-content: center;
    letter-spacing: -0.2px;
  }

  /* 728 x 90 */
  .leaderboard { left: 40px; top: 63px; width: 728px; height: 90px; }
  .leaderboard .green-field { position: absolute; left: 208px; top: 0; width: 520px; height: 90px; background: var(--green); }
  .leaderboard .brand { left: 23px; top: 12px; width: 158px; height: 66px; }
  .leaderboard .headline { left: 233px; top: 12px; font-size: 26px; }
  .leaderboard .support { left: 233px; top: 45px; color: var(--white); font-size: 14.5px; line-height: 20px; }
  .leaderboard .photo { left: 608px; top: 2px; width: 92px; height: 86px; }
  .leaderboard .cta { left: 590px; top: 61px; width: 131px; height: 27px; color: var(--ink); background: var(--pink-soft); }

  /* 160 x 600 */
  .skyscraper { left: 157px; top: 180px; width: 160px; height: 600px; }
  .skyscraper .wave { position: absolute; left: 0; top: 0; }
  .skyscraper .brand { left: 16px; top: 20px; width: 130px; height: 55px; }
  .skyscraper .brand-name { font-size: 18px; }
  .skyscraper .headline { left: 0; width: 160px; top: 110px; text-align: center; font-size: 28px; line-height: 36px; }
  .skyscraper .photo { left: 14px; top: 194px; width: 135px; height: 140px; }
  .skyscraper .support { left: 0; width: 160px; top: 360px; text-align: center; color: #111; font-size: 19.5px; line-height: 29px; }
  .skyscraper .cta { left: 14px; top: 551px; width: 134px; height: 33px; }

  /* 300 x 250 */
  .rectangle { left: 408px; top: 295px; width: 300px; height: 250px; }
  .rectangle .green-field { position: absolute; left: 0; top: 108px; width: 300px; height: 142px; background: var(--green); }
  .rectangle .brand { left: 83px; top: 15px; width: 130px; height: 52px; }
  .rectangle .brand-name { font-size: 18px; }
  .rectangle .headline { left: 0; width: 300px; top: 76px; text-align: center; font-size: 27px; }
  .rectangle .photo { left: 14px; top: 121px; width: 111px; height: 115px; }
  .rectangle .support { left: 140px; top: 121px; color: #111; font-size: 14.5px; line-height: 20px; }
  .rectangle .cta { left: 140px; top: 209px; width: 134px; height: 33px; border-color: var(--green-dark); font-size: 11px; }
</style>
</head>
<body>
<main class="board">

  <span class="size-label" style="left:670px; top:30px;">728 x 90</span>
  <section class="banner leaderboard" aria-label="728 by 90 banner">
    <div class="green-field"></div>
    <div class="brand"><span class="brand-name">Tidy Hearth</span></div>
    <h2 class="headline">Kick Chaos to the Curb</h2>
    <p class="support">Get your STUFF, your CALENDAR, &amp; your GOALS<br>TOTALLY UNDER CONTROL IN JUST 30-DAYS.</p>
    <div class="photo" role="img" aria-label="Photo of a tidy white wall organizer with file bins and a pinboard"></div>
    <a class="cta">Click here to learn more</a>
  </section>

  <section class="banner skyscraper" aria-label="160 by 600 banner">
    <svg class="wave" width="160" height="600" viewBox="0 0 160 600" aria-hidden="true">
      <path d="M0 262 C60 258 120 238 160 212 V600 H0 Z" fill="var(--pink)"/>
      <path d="M0 278 C60 274 120 256 160 236 V600 H0 Z" fill="var(--green)"/>
    </svg>
    <div class="brand"><span class="brand-name">Tidy Hearth</span></div>
    <h2 class="headline">Kick Chaos<br>to the Curb</h2>
    <div class="photo" role="img" aria-label="Photo of a tidy white wall organizer with file bins and a pinboard"></div>
    <p class="support">Get your Stuff,<br>your Calendar,<br>&amp; your Goals<br>totally under<br>control in just<br>30-Days.</p>
    <a class="cta">Click here to learn more</a>
  </section>
  <span class="size-label" style="left:332px; top:752px;">160 x 600</span>

  <section class="banner rectangle" aria-label="300 by 250 banner">
    <div class="green-field"></div>
    <div class="brand"><span class="brand-name">Tidy Hearth</span></div>
    <h2 class="headline">Kick Chaos to the Curb</h2>
    <div class="photo" role="img" aria-label="Photo of a tidy white wall organizer with file bins and a pinboard"></div>
    <p class="support">Get your Stuff, your<br>Calendar, &amp; your Goals<br>totally under control in<br>just 30-Days.</p>
    <a class="cta">Click here to learn more</a>
  </section>
  <span class="size-label" style="left:603px; top:561px;">300 x 250</span>

</main>
</body>
</html>
```